Southern Rigline Academy needs a modern website that oozes professionalism

Our current website is boring and looks like everyone elses. We need a modern website that says we are the best at plant operator training. We use Varnhold and Delvaro equipment for our training. We train all over Australia in Civil Construction, Mining and Quarrying. We want to be the "Go to" website for all plant operator training in Australia.

Industry/Entity Type

Heavy Machinery Training

Colors
0054AA
0677BA
7BADD7
CADEEF
E8F1F8
FFF300
FFF600
FEFA6F
FFFEC7
FFFEE8

```html
<!DOCTYPE html>
<html lang="en">
<head>
<meta charset="utf-8">
<title>Southern Rigline Academy — Plant Operator Training</title>
<link href="https://fonts.googleapis.com/css2?family=Fira+Sans:wght@500;600;700&family=Open+Sans:wght@400;600;700&display=swap" rel="stylesheet">
<style>
:root{
  --navy:#1c4077;
  --navy-deep:#16314f;
  --gold:#f7c31a;
  --ink:#2b2b2b;
  --muted:#6b6f76;
  --pale:#eef3f7;
  --card:#f4f4f4;
  --white:#fff;
}
*{box-sizing:border-box;margin:0;padding:0}
html,body{width:1200px;height:3825px;overflow:hidden}
body{position:relative;font-family:"Open Sans",sans-serif;color:var(--ink);background:var(--white)}
.abs{position:absolute}
h1,h2,h3{font-family:"Fira Sans",sans-serif}

/* header */
.site-header{left:0;top:0;width:1200px;height:67px;background:#fff;z-index:3}
.brand{left:107px;top:20px;display:flex;align-items:center;gap:8px;font-family:"Open Sans",sans-serif;font-weight:700;font-size:12px;color:var(--navy);letter-spacing:.5px}
.brand .dot{width:24px;height:24px;border-radius:50%;background:var(--navy)}
.main-nav{left:353px;top:24px;display:flex;gap:0}
.main-nav a{position:absolute;font-weight:700;font-size:14px;color:#333;text-decoration:none;white-space:nowrap}
.quote-btn{left:888px;top:0;width:312px;height:67px;background:var(--navy);color:#fff;font-weight:700;font-size:14px;letter-spacing:.5px;display:flex;align-items:center;padding-left:38px;gap:38px}

/* hero */
.hero{left:0;top:67px;width:1200px;height:574px;background:linear-gradient(180deg,#8a9aa8 0%,#a7aeb0 35%,#6f6a60 65%,#5a5148 100%)}
.hero-panel{left:91px;top:232px;width:496px;height:300px;background:rgba(30,30,30,.82)}
.hero-bar{left:91px;top:273px;width:5px;height:84px;background:var(--gold)}
.hero h1{left:118px;top:266px;width:460px;font-size:37px;line-height:50px;font-weight:600;color:#fff;letter-spacing:.6px}
.hero p{left:119px;top:377px;width:460px;font-size:14.5px;line-height:28px;color:#fff}
.btn-demo{left:117px;top:456px;width:198px;height:42px;background:var(--gold);color:#fff;font-weight:700;font-size:14px;display:flex;align-items:center;justify-content:center}

/* features */
.feature{top:736px;width:300px;display:flex;gap:10px}
.feature .ic{width:54px;height:54px;border-radius:50%;background:var(--navy);display:flex;align-items:center;justify-content:center;flex:none}
.feature h3{font-family:"Open Sans",sans-serif;font-size:15px;font-weight:700;color:#222;margin-top:0}
.feature p{font-size:12.5px;line-height:16px;color:#444}

/* about */
.about-bg{left:267px;top:940px;width:933px;height:410px;background:var(--pale);border-bottom-left-radius:90px}
.about-frame{left:144px;top:924px;width:364px;height:372px;border:5px solid var(--gold);border-radius:4px}
.about-photo{left:125px;top:903px;width:364px;height:374px;border-radius:4px;background:linear-gradient(160deg,#8fa7b9 0%,#c9b98a 40%,#e07a2a 60%,#3b4c7a 85%)}
.eyebrow{font-size:13px;color:#555;letter-spacing:.3px}
.about-text{left:563px;top:980px;width:520px}
.about-text h2{font-size:31px;font-weight:600;color:var(--navy);margin:6px 0 10px;letter-spacing:.5px}
.about-text p{font-size:13.5px;line-height:23.5px;color:#555;margin-bottom:2px}

/* section headings */
.sec-label{width:1200px;left:0;display:flex;justify-content:center;align-items:center;gap:14px;font-size:12px;font-weight:600;color:var(--gold)}
.sec-label i{display:block;width:48px;height:2px;background:var(--gold)}
.sec-title{width:1200px;left:0;text-align:center;font-size:46px;font-weight:600;color:var(--navy);letter-spacing:.8px}

/* services */
.services-bg{left:0;top:1520px;width:1200px;height:420px;background:linear-gradient(180deg,#fff 0%,#eef4f9 100%)}
.svc{top:1579px;width:302px;height:245px;background:#fff;border-radius:6px;box-shadow:0 3px 12px rgba(0,0,0,.08);overflow:hidden}
.svc .pic{height:143px}
.svc h3{display:flex;align-items:center;gap:8px;font-family:"Open Sans",sans-serif;font-size:18px;font-weight:600;color:var(--navy);margin:16px 0 6px 16px}
.svc p{font-size:13px;line-height:17px;color:#444;margin-left:16px;width:250px}

/* cta */
.cta{left:0;top:1935px;width:1200px;height:356px}
.cta h2{left:0;top:2015px;width:1200px;text-align:center;font-size:39px;line-height:46px;font-weight:600;color:#fff}
.cta p{left:0;top:2117px;width:1200px;text-align:center;font-size:19px;color:#fff}
.btn-contact{left:510px;top:2173px;width:179px;height:41px;border-radius:21px;background:var(--gold);color:#fff;font-size:14px;font-weight:600;display:flex;align-items:center;justify-content:center;gap:6px}

/* testimonials */
.review{top:2487px;width:322px;height:176px;background:var(--card);border-radius:3px;padding:40px 50px;text-align:center;font-size:12.5px;line-height:23px;color:#888}
.review.active{background:var(--navy);color:#fff}
.pointer{top:2663px;width:0;height:0;border-left:25px solid transparent;border-right:25px solid transparent;border-top:20px solid var(--navy)}
.avatar{top:2697px;width:44px;height:44px;border-radius:50%;background:linear-gradient(180deg,#9aa6b2,#4f5b68)}
.who{top:2752px;width:160px;text-align:center;font-size:9px;color:#333}
.who b{display:block;font-weight:700}
.who span{color:#888}

/* contact */
.contact-bg{left:0;top:2847px;width:1200px;height:600px;background:var(--pale)}
.contact-card{top:3032px;width:302px;height:243px;background:#fff;text-align:center}
.contact-card svg{margin-top:34px}
.contact-card h4{font-size:14px;font-weight:400;color:#222;margin-top:18px;letter-spacing:.3px}
.contact-card .l1{font-size:14px;color:var(--gold);margin-top:6px}
.contact-card .l2{font-size:14px;color:#222;margin-top:3px}
.contact-card .l1.blue{color:#3b6fb5}
.card-link{display:inline-flex;gap:8px;align-items:center;margin-top:22px;font-size:12px;color:var(--gold);border-bottom:2px solid var(--gold);padding:0 0 4px 0;width:104px;justify-content:center}

/* footer */
.footer{left:0;top:3380px;width:1200px;height:445px}
.f-brand{left:452px;top:3518px;width:296px;display:flex;align-items:center;justify-content:center;gap:10px;font-size:22px;font-weight:700;color:#fff;letter-spacing:.6px}
.f-brand .dot{width:34px;height:34px;border-radius:50%;background:#fff}
.f-about{left:450px;top:3612px;width:300px;text-align:center;font-size:12px;line-height:21px;color:#fff}
.social{top:3696px;width:35px;height:35px;border:1px solid rgba(255,255,255,.8)}
.f-col h5{font-size:16px;font-weight:700;color:#fff;letter-spacing:.3px}
.f-contact{left:92px;top:3562px;width:260px}
.f-row{display:flex;gap:16px;font-size:12px;line-height:20px;color:#fff;margin-top:16px;align-items:flex-start}
.f-hours{left:860px;top:3562px;width:246px;text-align:right}
.f-hours .h{display:flex;justify-content:flex-end;align-items:center;gap:16px;font-size:12px;color:#fff;margin-top:17px}
.f-hours u{color:#fff}
.f-rule{left:62px;top:3776px;width:1076px;height:1px;background:rgba(255,255,255,.3)}
.copyright{left:0;top:3792px;width:1200px;text-align:center;font-size:12.5px;color:#c8d1dc}
</style>
</head>
<body>

<header class="site-header abs">
  <div class="brand abs"><span class="dot"></span>SOUTHERN RIGLINE ACADEMY</div>
  <nav class="main-nav abs">
    <a style="left:0">HOME</a>
    <a style="left:103px">ABOUT US</a>
    <a style="left:244px">SERVICES</a>
    <a style="left:372px">CONTACT US</a>
  </nav>
  <div class="quote-btn abs">
    <svg width="12" height="18" viewBox="0 0 12 18"><path d="M2 2l7 7-7 7" fill="none" stroke="#fff" stroke-width="2"/></svg>
    GET QUOTATION
  </div>
</header>

<section class="hero abs" role="img" aria-label="Large yellow mining haul truck on a gravel quarry road under a cloudy sky"></section>
<div class="hero-panel abs"></div>
<div class="hero-bar abs"></div>
<div class="hero">
  <h1 class="abs">Empowering Operators, Fueling Progress</h1>
  <p class="abs">It is a long and established fact that a reader will be distracted by the readable content of a page when looking.</p>
  <div class="btn-demo abs">REQUEST A DEMO</div>
</div>

<!-- features -->
<div class="feature abs" style="left:125px">
  <div class="ic"><svg width="22" height="22" viewBox="0 0 24 24" fill="none" stroke="#fff" stroke-width="1.6"><circle cx="12" cy="12" r="4"/><path d="M12 2v3M12 19v3M2 12h3M19 12h3M5 5l2 2M17 17l2 2M5 19l2-2M17 7l2-2"/></svg></div>
  <div><h3>Expertise</h3><p>Lorem ipsum dolor sit amet, consectetu r adipiscing elit, sed do eiusmod</p></div>
</div>
<div class="feature abs" style="left:450px">
  <div class="ic"><svg width="22" height="22" viewBox="0 0 24 24" fill="none" stroke="#fff" stroke-width="1.6"><circle cx="12" cy="12" r="9"/><path d="M3 12h18M12 3c3 3 3 15 0 18M12 3c-3 3-3 15 0 18"/></svg></div>
  <div><h3>Professional</h3><p>Lorem ipsum dolor sit amet, consectetu r adipiscing elit, sed do eiusmod</p></div>
</div>
<div class="feature abs" style="left:775px">
  <div class="ic"><svg width="22" height="22" viewBox="0 0 24 24" fill="none" stroke="#fff" stroke-width="1.6"><circle cx="12" cy="8" r="4"/><path d="M4 21c0-4 4-6 8-6s8 2 8 6z"/></svg></div>
  <div><h3>Experienced</h3><p>Lorem ipsum dolor sit amet, consectetu r adipiscing elit, sed do eiusmod</p></div>
</div>

<!-- about -->
<div class="about-bg abs"></div>
<div class="about-frame abs"></div>
<div class="about-photo abs" role="img" aria-label="Site supervisor in hard hat and high-visibility vest directing a loader at a quarry"></div>
<div class="about-text abs">
  <div class="eyebrow">ABOUT US</div>
  <h2>Training for Industry Leaders</h2>
  <p>Lorem ipsum dolor sit amet, consectetur adipiscing elit, sed do eiusmod tempor incididunt ut labore et dolore magna aliqua. Ut enim ad minim veniam, quis n ostrud exercitation ullamco laboris nisi ut aliquip ex ea commodo consequat. Duis aute irure dolor in reprehenderit in voluptate velit esse cillum dolore eu fugiat nulla pariatur. Excepteur sint occaecat cupidatat non proident, sunt in culpa qui officia deserunt mollit anim id est laborum.</p>
  <p>Lorem ipsum dolor sit amet, consectetur adipiscing elit, sed do eiusmod tempor incididunt ut labore et dolore magna aliqua. Ut enim ad minim veniam, quis n ostrud exercitation ullamco laboris nisi ut aliquip ex ea commodo consequat. Duis aute irure dolor in reprehenderit</p>
</div>

<!-- services -->
<div class="services-bg abs"></div>
<div class="sec-label abs" style="top:1446px"><i></i>SERVICES<i></i></div>
<h2 class="sec-title abs" style="top:1470px">Services We Provide</h2>

<div class="svc abs" style="left:125px">
  <div class="pic" role="img" aria-label="Engineer in safety glasses beside an excavator on a civil construction site" style="background:linear-gradient(120deg,#2b3550 0%,#6f8aa6 45%,#d9b545 80%,#8a7a55 100%)"></div>
  <h3><svg width="17" height="17" viewBox="0 0 20 20"><circle cx="10" cy="10" r="9" fill="#777"/><path d="M6 10l3 3 5-6" fill="none" stroke="#fff" stroke-width="2"/></svg>Civil Construction</h3>
  <p>Lorem ipsum is simply dummy text of the printing and typesetting...</p>
</div>
<div class="svc abs" style="left:450px">
  <div class="pic" role="img" aria-label="Mine worker in orange hard hat and vest at an open-cut mine" style="background:linear-gradient(120deg,#d87a3a 0%,#f0b060 40%,#f3d8b0 70%,#c9a27a 100%)"></div>
  <h3><svg width="17" height="17" viewBox="0 0 20 20"><circle cx="10" cy="10" r="9" fill="#777"/><path d="M6 10l3 3 5-6" fill="none" stroke="#fff" stroke-width="2"/></svg>Mining</h3>
  <p>Lorem ipsum is simply dummy text of the printing and typesetting...</p>
</div>
<div class="svc abs" style="left:772px">
  <div class="pic" role="img" aria-label="Yellow excavator loading sand at a quarry" style="background:linear-gradient(120deg,#a8743a 0%,#d9a55a 40%,#e8c078 70%,#b98a4e 100%)"></div>
  <h3><svg width="17" height="17" viewBox="0 0 20 20"><circle cx="10" cy="10" r="9" fill="#777"/><path d="M6 10l3 3 5-6" fill="none" stroke="#fff" stroke-width="2"/></svg>Quarrying</h3>
  <p>Lorem ipsum is simply dummy text of the printing and typesetting...</p>
</div>

<!-- cta band -->
<svg class="cta abs" width="1200" height="356" viewBox="0 0 1200 356" role="img" aria-label="Haul truck silhouetted against an orange sunset over a mine site">
  <defs>
    <linearGradient id="ctaFill" x1="0" y1="0" x2="0" y2="1">
      <stop offset="0" stop-color="#3f3f45"/>
      <stop offset=".55" stop-color="#4f4a4c"/>
      <stop offset=".8" stop-color="#8a5a36"/>
      <stop offset="1" stop-color="#2a2a30"/>
    </linearGradient>
  </defs>
  <path d="M0 30 Q600 -30 1200 20 L1200 320 Q600 400 0 300 Z" fill="url(#ctaFill)"/>
</svg>
<div class="cta">
  <h2 class="abs">Where Operators Thrive<br>and Industries Flourish</h2>
  <p class="abs">Get in touch with us for the best experienced professional services</p>
  <div class="btn-contact abs">CONTACT US <svg width="12" height="10" viewBox="0 0 12 10"><path d="M0 5h10M6 1l4 4-4 4" fill="none" stroke="#fff" stroke-width="1.5"/></svg></div>
</div>

<!-- testimonials -->
<div class="sec-label abs" style="top:2370px"><i></i>TESTIMONIALS<i></i></div>
<h2 class="sec-title abs" style="top:2393px">Client Reviews</h2>

<div class="review abs" style="left:92px">Lorem ipsum dolor sit amet, consec tetur adipiscing elit, sed do eius mod tempor incididunt ut labore e t dolore magna aliqua.</div>
<div class="review active abs" style="left:438px">Lorem ipsum dolor sit amet, consec tetur adipiscing elit, sed do eius mod tempor incididunt ut labore e t dolore magna aliqua.</div>
<div class="review abs" style="left:786px">Lorem ipsum dolor sit amet, consec tetur adipiscing elit, sed do eius mod tempor incididunt ut labore e t dolore magna aliqua.</div>

<div class="pointer abs" style="left:228px"></div>
<div class="pointer abs" style="left:573px"></div>
<div class="pointer abs" style="left:921px"></div>

<div class="avatar abs" style="left:231px" role="img" aria-label="Customer portrait"></div>
<div class="avatar abs" style="left:576px" role="img" aria-label="Customer portrait"></div>
<div class="avatar abs" style="left:924px" role="img" aria-label="Customer portrait"></div>

<div class="who abs" style="left:173px"><b>Dean Holloway</b><span>Customer</span></div>
<div class="who abs" style="left:518px"><b>Dean Holloway</b><span>Customer</span></div>
<div class="who abs" style="left:866px"><b>Dean Holloway</b><span>Customer</span></div>

<!-- contact -->
<div class="contact-bg abs"></div>
<div class="sec-label abs" style="top:2908px"><i></i>CONTACT US<i></i></div>
<h2 class="sec-title abs" style="top:2931px">Get in touch with us</h2>

<div class="contact-card abs" style="left:131px">
  <svg width="44" height="40" viewBox="0 0 44 40" fill="none" stroke="#f7c31a" stroke-width="1.8"><path d="M22 4a8 8 0 0 1 8 8c0 7-8 15-8 15s-8-8-8-15a8 8 0 0 1 8-8z"/><circle cx="22" cy="12" r="3"/><path d="M10 26l-6 12h36l-6-12"/></svg>
  <h4>FIND US</h4>
  <div class="l1">ABD Avenue</div>
  <div class="l2">City, District, Country</div>
  <div class="card-link">CONTACT US <svg width="12" height="10" viewBox="0 0 12 10"><path d="M0 5h10M6 1l4 4-4 4" fill="none" stroke="#f7c31a" stroke-width="1.5"/></svg></div>
</div>
<div class="contact-card abs" style="left:456px">
  <svg width="40" height="40" viewBox="0 0 40 40" fill="none" stroke="#f7c31a" stroke-width="1.8"><path d="M8 4l7 0 3 9-5 3c2 5 6 9 11 11l3-5 9 3v7c0 2-2 3-4 3C18 35 5 22 5 8c0-2 1-4 3-4z"/></svg>
  <h4>CALL US AT</h4>
  <div class="l1 blue">(123) 456-7890</div>
  <div class="l2">info@company.com</div>
  <div class="card-link">CONTACT US <svg width="12" height="10" viewBox="0 0 12 10"><path d="M0 5h10M6 1l4 4-4 4" fill="none" stroke="#f7c31a" stroke-width="1.5"/></svg></div>
</div>
<div class="contact-card abs" style="left:781px">
  <svg width="40" height="40" viewBox="0 0 40 40" fill="none" stroke="#f7c31a" stroke-width="1.8"><path d="M4 16l16-12 16 12v20H4z"/><path d="M4 16l16 12 16-12"/><circle cx="20" cy="15" r="5"/></svg>
  <h4>EMAIL US</h4>
  <div class="l1">(123) 456-7890</div>
  <div class="l2">info@company.com</div>
  <div class="card-link">CONTACT US <svg width="12" height="10" viewBox="0 0 12 10"><path d="M0 5h10M6 1l4 4-4 4" fill="none" stroke="#f7c31a" stroke-width="1.5"/></svg></div>
</div>

<!-- footer -->
<svg class="footer abs" width="1200" height="445" viewBox="0 0 1200 445">
  <path d="M0 40 Q600 -30 1200 20 L1200 445 L0 445 Z" fill="#d6e8f3"/>
  <path d="M0 62 Q600 -10 1200 40 L1200 445 L0 445 Z" fill="#16314f"/>
</svg>
<div class="f-brand abs"><span class="dot"></span>SOUTHERN RIGLINE ACADEMY</div>
<p class="f-about abs">Lorem ipsum dolor sit amet, consectetur adipisc ing elit, sed do eiusmod tempor incididunt ut labore et dolore magna aliqua</p>
<div class="social abs" style="left:537px"></div>
<div class="social abs" style="left:581px"></div>
<div class="social abs" style="left:625px"></div>

<div class="f-col f-contact abs">
  <h5>CONTACT US</h5>
  <div class="f-row"><svg width="14" height="20" viewBox="0 0 14 20"><path d="M7 0a7 7 0 0 1 7 7c0 5-7 13-7 13S0 12 0 7a7 7 0 0 1 7-7z" fill="#fff"/><circle cx="7" cy="7" r="2.5" fill="#16314f"/></svg><span>101- lorem ipsum simple text<br>print type text industry text.</span></div>
  <div class="f-row"><svg width="14" height="14" viewBox="0 0 14 14"><path d="M2 0h3l1 4-2 1c1 2 3 4 5 5l1-2 4 1v3c0 1-1 2-2 2C6 14 0 8 0 2 0 1 1 0 2 0z" fill="#fff"/></svg><span>123 456 7890</span></div>
  <div class="f-row"><svg width="16" height="12" viewBox="0 0 16 12"><rect width="16" height="12" fill="#fff"/><path d="M0 0l8 7 8-7" fill="none" stroke="#16314f" stroke-width="1.4"/></svg><span>info@company.com</span></div>
</div>

<div class="f-col f-hours abs">
  <h5>OPENING HOURS</h5>
  <div class="h">Mon - Fri: 9am - to - 6pm <svg width="16" height="16" viewBox="0 0 16 16" fill="none" stroke="#fff" stroke-width="1.4"><circle cx="8" cy="8" r="7"/><path d="M8 4v4h3"/></svg></div>
  <div class="h">Saturday 9am - to - 2pm <svg width="16" height="16" viewBox="0 0 16 16" fill="none" stroke="#fff" stroke-width="1.4"><circle cx="8" cy="8" r="7"/><path d="M8 4v4h3"/></svg></div>
  <div class="h"><span>Sunday : <u>Closed</u></span> <svg width="16" height="16" viewBox="0 0 16 16" fill="none" stroke="#fff" stroke-width="1.4"><circle cx="8" cy="8" r="7"/><path d="M8 4v4h3"/></svg></div>
</div>

<div class="f-rule abs"></div>
<div class="copyright abs">Southern Rigline Academy</div>

</body>
</html>
```